Lawn sign for construction company

Would like this to be a very clean and high end design for luxury homes. We need a yard sign designed that includes the company logo, website, phone number and major service offerings (residential and commercial renovations and maintenance)
The company website is brambleworks.com all other contact info is in the attachments
Target Market(s)
Luxury home owners and business owners
Industry/Entity Type
Construction/Home Improvement
Font styles to use
Other font styles liked:
- See company logo and other graphics included for title text fonts. All other fonts can be standard sans serif.
Colors
0054AA
0677BA
7BADD7
CADEEF
E8F1F8
Requirements
Must have
- Clean, easy to read design, would like 2 sided sign. A main sign side and back side which states “free estimates, and includes the website and phone number. Must also match the color scheme of the provided logo and other company images. Dark Navy blue primary color, gray secondary color, and orange as an accent color.
Nice to have
- 2nd sign side very simple design
Should not have
- Too many graphics limit to 1-3 colors

```html
<!DOCTYPE html>
<html lang="en">
<head>
<meta charset="utf-8">
<title>Bramble Works – Yard Sign, Two Sides</title>
<link rel="stylesheet" href="https://fonts.googleapis.com/css2?family=Barlow+Condensed:wght@700&family=Montserrat:wght@700;800&display=swap">
<style>
  :root{
    --navy:#0d2452;
    --orange:#f08200;
    --white:#ffffff;
    --backdrop:#e6e7e9;
  }
  *{margin:0;padding:0;box-sizing:border-box;}
  html,body{width:1200px;height:2665px;overflow:hidden;}
  body{
    background:var(--backdrop);
    display:flex;flex-direction:column;align-items:center;justify-content:center;gap:200px;
  }
  .sign{
    position:relative;width:1000px;height:746px;background:var(--white);
    box-shadow:0 6px 24px rgba(0,0,0,.12);overflow:hidden;
  }
  .sign-bands{position:absolute;inset:0;width:100%;height:100%;}
  .band-accent{fill:var(--orange);}
  .band-base{fill:var(--navy);}
  .line{position:absolute;left:0;right:0;text-align:center;white-space:nowrap;}

  /* Front side */
  .brand-name{
    top:160px;font-family:"Montserrat",sans-serif;font-weight:700;font-size:92px;
    color:var(--navy);line-height:1;letter-spacing:0;
  }
  .services-kicker{
    top:500px;font-family:"Barlow Condensed",sans-serif;font-weight:700;
    font-size:58px;color:var(--orange);line-height:1;
  }
  .services-main{
    font-family:"Montserrat",sans-serif;font-weight:700;font-size:70px;
    color:var(--white);line-height:1;
  }
  .services-main.first{top:570px;}
  .services-main.second{top:648px;}

  /* Back side */
  .offer-big{
    top:50px;font-family:"Montserrat",sans-serif;font-weight:800;font-size:240px;
    color:var(--orange);line-height:1;letter-spacing:-4px;
  }
  .offer-sub{
    top:285px;font-family:"Montserrat",sans-serif;font-weight:800;font-size:108px;
    color:var(--navy);line-height:1;letter-spacing:-2px;
  }
  .contact{
    position:absolute;left:145px;display:flex;align-items:center;gap:40px;
    font-family:"Montserrat",sans-serif;font-weight:700;color:var(--white);line-height:1;
  }
  .contact svg{flex:none;}
  .contact.web{top:520px;font-size:56px;}
  .contact.phone{top:600px;font-size:82px;}
  .icon-stroke{fill:none;stroke:var(--orange);stroke-width:4;}
  .icon-fill{fill:var(--orange);}
</style>
</head>
<body>

<section class="sign sign-front" aria-label="Sign front side">
  <svg class="sign-bands" viewBox="0 0 1000 746" preserveAspectRatio="none" aria-hidden="true">
    <polygon class="band-accent" points="0,376 500,462 1000,376 1000,405 500,462 0,405"/>
    <polygon class="band-base" points="0,405 500,462 1000,405 1000,746 0,746"/>
  </svg>
  <p class="line brand-name">Bramble Works</p>
  <p class="line services-kicker">RESIDENTIAL AND COMMERCIAL</p>
  <p class="line services-main first">RENOVATIONS AND</p>
  <p class="line services-main second">MAINTENANCE</p>
</section>

<section class="sign sign-back" aria-label="Sign back side">
  <svg class="sign-bands" viewBox="0 0 1000 746" preserveAspectRatio="none" aria-hidden="true">
    <polygon class="band-accent" points="0,376 500,462 1000,376 1000,405 500,462 0,405"/>
    <polygon class="band-base" points="0,405 500,462 1000,405 1000,746 0,746"/>
  </svg>
  <p class="line offer-big">FREE</p>
  <p class="line offer-sub">ESTIMATES</p>

  <div class="contact web">
    <svg width="46" height="46" viewBox="0 0 46 46" aria-hidden="true">
      <circle class="icon-stroke" cx="23" cy="23" r="19"/>
      <ellipse class="icon-stroke" cx="23" cy="23" rx="8" ry="19"/>
      <line class="icon-stroke" x1="4" y1="23" x2="42" y2="23"/>
      <line class="icon-stroke" x1="7" y1="13" x2="39" y2="13"/>
      <line class="icon-stroke" x1="7" y1="33" x2="39" y2="33"/>
    </svg>
    <span>brambleworks.com</span>
  </div>

  <div class="contact phone">
    <svg width="52" height="52" viewBox="0 0 52 52" aria-hidden="true">
      <path class="icon-fill" d="M14 6c2-1 4 0 5 2l4 8c1 2 0 4-1 5l-3 3c2 5 6 9 11 11l3-3c1-1 3-2 5-1l8 4c2 1 3 3 2 5l-2 5c-1 2-3 3-5 3C22 47 5 30 4 11c0-2 1-4 3-5z"/>
      <path class="icon-stroke" d="M30 8a14 14 0 0 1 14 14M30 15a7 7 0 0 1 7 7"/>
    </svg>
    <span>(555) 014-7720</span>
  </div>
</section>

</body>
</html>
```